Web Design Project

We need a web design company for a company based in London. We are an online minicab booking service that produces real time quotes on cab journey for consumers. Our colours are currently red and yellow, but do not need to stay that way; it's open to interpretation. Please avoid yellow and black as a colour combination. Our current site is: www.rovelto.co.uk We are looking for a new site to be user-friendly and easy to use, but more polished and professional looking, without using it usability and simplicity. We need to keep the booking capability on each page and it needs to draw in the user's eye. We need a site that is reliable and easy to use, but also fun.

Main objective: keep it simple, like it is now, but polish it up some. Also, we need to be able to add more content to it. And, we will also be adding a login capability for return users.

Target Market(s)

Internet-savvy people aged 18 and older.

Industry/Entity Type

It Company

Requirements
Must have
• Must have the booking widget. However, it doesn't have to be as large as it is now. We are actually thinking to split it over two pages. We will add a few options to the booking widget, such as another via option. The booking widget must be the most noticeable feature on the page. Sans serif font, please.
Should not have
• Should not be too busy and distracting. Please do not use any images of traditional taxis, ie. black cabs from London or yellow cabs from NYC. Our cars do not resemble these and our business cannot be associated with these images.

```html
<!DOCTYPE html>
<html lang="en">
<head>
<meta charset="utf-8">
<title>Rovelto – How it works</title>
<link rel="stylesheet" href="https://fonts.googleapis.com/css2?family=Arimo:ital,wght@0,400;0,700;1,400&family=Open+Sans:wght@400;700&family=Roboto+Condensed:wght@700&display=swap">
<style>
  :root {
    --orange: #c4500b;
    --orange-dark: #a8430a;
    --brown: #8a3e0d;
    --topbar: #3b3b3b;
    --page: #f7f6f4;
    --ink: #222222;
    --text: #444444;
    --muted: #888888;
    --panel: #f1f1f0;
    --panel-line: #c9c9c9;
    --button: #2b2b2b;
    --footer-top: #2a2a2a;
    --footer-mid: #4a4a4a;
    --white: #ffffff;
    --link: #2a4fc4;
    --social: #cfcfcf;
  }
  * { box-sizing: border-box; margin: 0; padding: 0; }
  html, body { width: 831px; height: 1200px; overflow: hidden; }
  body { background: var(--page); font-family: "Arimo", Arial, sans-serif; color: var(--text); position: relative; }

  /* Header */
  .site-header { position: absolute; left: 0; top: 0; width: 831px; height: 78px; background: var(--orange); border-top: 5px solid var(--topbar); border-bottom: 1px solid var(--orange-dark); }
  .brand { position: absolute; left: 80px; top: 16px; display: flex; align-items: center; gap: 8px; font-family: "Arimo", Arial, sans-serif; font-weight: 700; font-size: 30px; color: var(--white); }
  .brand-mark { width: 14px; height: 14px; border-radius: 50%; background: var(--white); }
  .main-nav { position: absolute; top: 28px; left: 309px; display: flex; align-items: center; font-family: "Open Sans", Arial, sans-serif; font-size: 12px; color: var(--ink); }
  .main-nav .nav-item { padding: 4px 8px; }
  .main-nav .nav-item.is-active { background: var(--orange-dark); color: #f3d6c3; border-radius: 2px; }
  .main-nav .miles { margin-right: 23px; }
  .main-nav .join { margin-right: 18px; }
  .main-nav .about { margin-right: 20px; }
  .account { position: absolute; top: 32px; left: 686px; font-family: "Open Sans", Arial, sans-serif; font-size: 11px; color: var(--white); }
  .account a { color: var(--white); }
  .account .sep { margin: 0 12px; }

  /* How it works */
  .how-it-works { position: absolute; left: 0; top: 78px; width: 831px; height: 313px; background: var(--orange); border-bottom: 2px solid #e9b796; color: var(--white); font-family: "Open Sans", Arial, sans-serif; }
  .how-title { position: absolute; top: 32px; width: 100%; text-align: center; font-family: "Arimo", Arial, sans-serif; font-size: 31px; font-weight: 700; letter-spacing: 0.5px; }
  .step { position: absolute; top: 98px; display: flex; align-items: center; gap: 22px; font-size: 14px; line-height: 17px; }
  .step-icon { width: 56px; height: 56px; border-radius: 50%; background: var(--topbar); display: flex; align-items: center; justify-content: center; flex: none; }
  .step-1 { left: 51px; }
  .step-2 { left: 287px; }
  .step-3 { left: 553px; }
  .tagline { position: absolute; top: 213px; width: 100%; text-align: center; font-size: 22px; }
  .tagline-sub { position: absolute; top: 247px; width: 100%; text-align: center; font-size: 14px; }

  /* Booking widget */
  .booking { position: absolute; left: 44px; top: 436px; width: 232px; height: 591px; background: var(--panel); border: 1px solid var(--panel-line); }
  .booking-title { height: 36px; padding: 10px 13px; font-size: 13px; font-weight: 400; color: var(--ink); background: #e6e6e5; border-bottom: 1px solid var(--panel-line); letter-spacing: 0.3px; }
  .booking-body { position: relative; height: 553px; }
  .field-label { position: absolute; left: 14px; font-size: 11px; color: var(--ink); }
  .input { position: absolute; left: 14px; height: 23px; background: var(--white); border: 1px solid #cccccc; font-size: 9px; font-style: italic; color: var(--muted); padding: 6px 8px; }
  .input.plain { font-style: normal; }
  .find-btn { position: absolute; left: 171px; width: 47px; height: 23px; background: var(--button); color: var(--white); font-size: 10px; font-weight: 700; text-align: center; line-height: 23px; }
  .calendar { position: absolute; left: 186px; top: 131px; }
  .select { position: absolute; height: 14px; border: 1px solid #cccccc; background: var(--white); }
  .select::after { content: ""; position: absolute; right: 5px; top: 3px; border: 5px solid transparent; border-top: 6px solid var(--ink); border-bottom: 0; }
  .small-label { position: absolute; font-size: 9px; color: var(--ink); }
  .check { position: absolute; top: 223px; display: flex; align-items: center; gap: 8px; font-size: 11px; color: var(--ink); }
  .box { width: 15px; height: 15px; border: 1px solid #bbbbbb; background: var(--white); display: inline-flex; align-items: center; justify-content: center; }
  .quote-btn { position: absolute; left: 18px; top: 499px; width: 196px; height: 28px; background: var(--button); border-radius: 3px; color: var(--white); font-size: 13px; text-align: center; line-height: 28px; box-shadow: 0 1px 2px rgba(0,0,0,0.4); }

  /* Content column */
  .why { position: absolute; left: 350px; top: 436px; width: 424px; }
  .section-title { font-family: "Roboto Condensed", "Arial Narrow", sans-serif; font-weight: 700; font-size: 23px; color: var(--brown); padding-bottom: 6px; border-bottom: 1px solid #b9b9b9; }
  .feature-title { margin-top: 20px; font-size: 12px; font-weight: 700; color: var(--ink); }
  .feature-title + .feature-text { margin-top: 10px; }
  .feature-text { font-size: 11px; line-height: 18px; color: var(--text); }
  .feature-title.tight { margin-top: 8px; }

  .stories { position: absolute; left: 350px; top: 700px; width: 424px; }
  .stories-title { font-size: 17px; font-weight: 700; color: var(--ink); padding-bottom: 8px; border-bottom: 1px solid #b9b9b9; }
  .story { margin-top: 16px; font-size: 10.4px; line-height: 18.7px; color: var(--text); }
  .story-cta { margin-top: 16px; font-size: 12px; font-style: italic; color: var(--ink); }
  .story-cta a { color: var(--link); }

  /* Footer */
  .site-footer { position: absolute; left: 0; top: 1107px; width: 831px; height: 93px; background: radial-gradient(ellipse at 50% 50%, var(--footer-mid) 0%, var(--footer-top) 75%); border-top: 3px solid #1d1d1d; color: var(--white); font-size: 9px; }
  .copyright { position: absolute; left: 51px; top: 21px; line-height: 14px; }
  .copyright a { color: #e0792f; }
  .copyright .policy { color: var(--white); }
  .follow { position: absolute; left: 636px; top: 17px; display: flex; align-items: center; gap: 8px; }
  .follow-label { margin-right: 8px; }
  .social-dot { width: 24px; height: 24px; border-radius: 50%; background: var(--social); }
</style>
</head>
<body>

<header class="site-header">
  <div class="brand"><span class="brand-mark"></span>Rovelto</div>
  <nav class="main-nav">
    <span class="nav-item is-active miles">Rovelto Miles</span>
    <span class="nav-item join">Join Us</span>
    <span class="nav-item about">About Us</span>
    <span class="nav-item">Contact Us</span>
  </nav>
  <div class="account"><a href="#">login</a><span class="sep">or</span><a href="#">sign up</a></div>
</header>

<section class="how-it-works">
  <h1 class="how-title">HOW IT WORKS?</h1>

  <div class="step step-1">
    <span class="step-icon">
      <svg width="24" height="28" viewBox="0 0 24 28"><rect x="1" y="1" width="22" height="26" fill="#fff"/><g stroke="#3b3b3b" stroke-width="2"><line x1="5" y1="7" x2="19" y2="7"/><line x1="5" y1="12" x2="19" y2="12"/><line x1="5" y1="17" x2="19" y2="17"/><line x1="5" y1="22" x2="14" y2="22"/></g></svg>
    </span>
    <span>Enter your route</span>
  </div>

  <div class="step step-2">
    <span class="step-icon">
      <svg width="32" height="30" viewBox="0 0 32 30" fill="none" stroke="#fff" stroke-width="2"><line x1="16" y1="3" x2="16" y2="26"/><line x1="4" y1="7" x2="28" y2="5"/><line x1="9" y1="27" x2="23" y2="27"/><path d="M1 17 L4 7 L7 17 Z" fill="#fff"/><path d="M25 15 L28 5 L31 15 Z" fill="#fff"/></svg>
    </span>
    <span>Quickly compare<br>taxi fares</span>
  </div>

  <div class="step step-3">
    <span class="step-icon">
      <svg width="30" height="22" viewBox="0 0 30 22"><rect x="1" y="1" width="28" height="20" fill="#fff"/><path d="M1 1 L15 13 L29 1" fill="none" stroke="#3b3b3b" stroke-width="2"/></svg>
    </span>
    <span>Get your travel con-<br>firmed on your phone by<br>SMS.</span>
  </div>

  <p class="tagline">As easy as opening the cab's door</p>
  <p class="tagline-sub">Its free, dependable and with no obligation</p>
</section>

<aside class="booking">
  <h2 class="booking-title">BOOK A CAB</h2>
  <div class="booking-body">
    <span class="field-label" style="top:19px">Pick me up from:</span>
    <span class="input" style="top:31px;width:157px">e.g.&nbsp; pick up address or post code</span>
    <span class="find-btn" style="top:31px">Find</span>

    <span class="field-label" style="top:71px">Drop me at:</span>
    <span class="input" style="top:83px;width:157px">e.g.&nbsp; drop address or post code</span>
    <span class="find-btn" style="top:83px">Find</span>

    <span class="field-label" style="top:122px">Pick up date and time:</span>
    <span class="input plain" style="top:134px;width:157px">5 Apr 2012 @ 12:02</span>
    <svg class="calendar" width="32" height="26" viewBox="0 0 32 26"><rect x="1" y="3" width="30" height="22" fill="#fff" stroke="#9aa7c0"/><rect x="1" y="3" width="30" height="6" fill="#3d5f9e"/><g fill="#9aa7c0"><rect x="5" y="12" width="4" height="3"/><rect x="11" y="12" width="4" height="3"/><rect x="17" y="12" width="4" height="3"/><rect x="23" y="12" width="4" height="3"/><rect x="5" y="18" width="4" height="3"/><rect x="11" y="18" width="4" height="3"/><rect x="17" y="18" width="4" height="3"/></g></svg>

    <span class="small-label" style="left:14px;top:177px">Just pick me up in</span>
    <span class="select" style="left:100px;top:176px;width:71px"></span>

    <span class="small-label" style="left:14px;top:201px">Passenger:</span>
    <span class="select" style="left:70px;top:200px;width:40px"></span>
    <span class="small-label" style="left:125px;top:201px">Luggage:</span>
    <span class="select" style="left:172px;top:200px;width:40px"></span>

    <span class="check" style="left:14px"><span class="box"><svg width="13" height="13" viewBox="0 0 13 13"><path d="M2 7 L5 11 L12 1" fill="none" stroke="#333" stroke-width="1.6"/></svg></span>Return Journey</span>
    <span class="check" style="left:126px"><span class="box"></span>Extras</span>

    <span class="field-label" style="top:251px">Mobile Number:</span>
    <span class="input" style="top:267px;width:204px"></span>
    <span class="field-label" style="top:302px">Name:</span>
    <span class="input" style="top:318px;width:204px"></span>
    <span class="field-label" style="top:353px">Email:</span>
    <span class="input" style="top:369px;width:204px"></span>
    <span class="field-label" style="top:405px">Comments:</span>
    <span class="input" style="top:421px;width:204px;height:53px"></span>

    <span class="quote-btn">Get your no obligation quotes</span>
  </div>
</aside>

<section class="why">
  <h2 class="section-title">Why Rovelto?</h2>
  <h3 class="feature-title">Price</h3>
  <p class="feature-text">Rovelto guarantees that you get the best deal for your travel, as you get quotes from several cab companies.</p>
  <h3 class="feature-title tight">No fees</h3>
  <p class="feature-text">There's absolutely no cost for you to use our service.</p>
  <h3 class="feature-title tight">Coverage</h3>
  <p class="feature-text">Rovelto has the largest database of licensed minicab operators. You can use Rovelto wherever you are in greater London.</p>
</section>

<section class="stories">
  <h2 class="stories-title">The best stories from our community</h2>
  <p class="story">I recently hit London for a girlie night on the town with my bestie. After a little too much champagne, we had a stupid argument and decided to leave the club early. In the cab on our way home, we didn't say one word to each other. The driver who could sense we were both upset however, had other plans. He randomly started singing Velmora's Midnight Waltz! My best friend and I were in shock, we looked at each other and couldn't stop laughing! The remainder of the journey consisted of us all belting out Velmora classics, in between fits of laughter. We were so disappointed when we arrived home as we wanted to continue the fun, we will never forget our singing taxi driver!</p>
  <p class="story-cta">Do you have your story? <a href="#">Send</a> us it!</p>
</section>

<footer class="site-footer">
  <p class="copyright">© <a href="#">Rovelto</a> 2011-2012. All rights reserved.<br><a class="policy" href="#">Privacy Policy</a></p>
  <div class="follow">
    <span class="follow-label">Follow Us:</span>
    <span class="social-dot"></span>
    <span class="social-dot"></span>
    <span class="social-dot"></span>
  </div>
</footer>

</body>
</html>
```